business card/stationary for dental office
Bright Harbor Dental Care
business card/stationary for dental office - Health
Creative Brief
Professional
R. Warren Halvik, DDS
Team Leader
2847 NW 42nd Ave Del City, OK 73115
info@brightharbordentalcare.example
brightharbordentalcare.example
I'll attach and example picture of what i want. text "NO INSURANCE, NO PROBLEM!". "Ask us about our Chairside Savings Plan."
quillmoth quillmoth
pbrandle pbrandle
definately want the back silver not blue

```html
<!DOCTYPE html>
<html lang="en">
<head>
<meta charset="utf-8">
<title>Bright Harbor Dental Care – Business Card</title>
<link href="https://fonts.googleapis.com/css2?family=Exo+2:wght@400;600;700&display=swap" rel="stylesheet">
<style>
  :root{
    --bg:#c9cbcd;
    --card:#ffffff;
    --card-back:#eef0f2;
    --card-back-shade:#dfe2e5;
    --blue:#1f7ae0;
    --ink:#2b2f36;
    --muted:#5d636b;
    --white:#ffffff;
  }
  *{box-sizing:border-box;margin:0;padding:0}
  html,body{width:1200px;height:895px;overflow:hidden}
  body{
    background:var(--bg);
    font-family:"Exo 2",sans-serif;
    display:flex;flex-direction:column;align-items:center;justify-content:center;gap:35px;
  }
  .card{
    position:relative;width:700px;height:400px;overflow:hidden;
    box-shadow:0 8px 24px rgba(0,0,0,.18);
  }
  .card--back{background:linear-gradient(135deg,var(--card-back),var(--card-back-shade))}
  .card--front{background:var(--card)}
  .corner-band{position:absolute;background:var(--blue)}
  .card--back .corner-band{right:0;top:62px;width:150px;height:30px}
  .card--front .corner-band{right:0;top:52px;width:205px;height:26px}

  .brand{display:flex;align-items:center;gap:10px}
  .brand__dot{flex-shrink:0;width:22px;height:22px;border-radius:50%;background:var(--blue)}
  .brand__name{font-weight:700;color:var(--blue);letter-spacing:.5px;line-height:1.05}

  .back-content{
    position:absolute;left:0;right:0;top:150px;
    display:flex;flex-direction:column;align-items:center;gap:26px;text-align:center;
  }
  .card--back .brand__name{font-size:34px;white-space:nowrap}
  .card--back .brand__dot{width:30px;height:30px}
  .offer__headline{font-size:20px;font-weight:700;color:var(--ink);letter-spacing:1.5px}
  .offer__line{font-size:15px;color:var(--muted);margin-top:6px;letter-spacing:.5px}

  .card--front .brand{position:absolute;left:34px;top:40px}
  .card--front .brand__name{font-size:22px}

  .person{position:absolute;right:40px;top:120px;text-align:right}
  .person__name{font-size:22px;font-weight:600;color:var(--ink);letter-spacing:1px;text-transform:uppercase}
  .person__role{font-size:13px;color:var(--muted);letter-spacing:1.5px;text-transform:uppercase;margin-top:2px}

  .contact-panel{
    position:absolute;left:0;right:22px;bottom:22px;height:190px;
    background:var(--blue);border-radius:0 16px 16px 0;
    display:grid;grid-template-columns:1fr 1.6fr 1.2fr;
  }
  .contact-panel__col{
    display:flex;flex-direction:column;align-items:center;justify-content:flex-start;
    padding:30px 8px 0;gap:18px;color:var(--white);font-size:14px;text-align:center;line-height:1.5;
  }
  .contact-panel__col + .contact-panel__col{border-left:1.5px solid rgba(255,255,255,.75)}
  .contact-panel__col svg{width:34px;height:34px}
</style>
</head>
<body>

<section class="card card--back" aria-label="Card back">
  <div class="corner-band"></div>
  <div class="back-content">
    <div class="brand">
      <span class="brand__dot"></span>
      <span class="brand__name">Bright Harbor Dental Care</span>
    </div>
    <div class="offer">
      <p class="offer__headline">NO INSURANCE, NO PROBLEM!</p>
      <p class="offer__line">Ask us about our Chairside Savings Plan.</p>
    </div>
  </div>
</section>

<section class="card card--front" aria-label="Card front">
  <div class="corner-band"></div>
  <div class="brand">
    <span class="brand__dot"></span>
    <span class="brand__name">Bright Harbor<br>Dental Care</span>
  </div>
  <div class="person">
    <p class="person__name">R. Warren Halvik, DDS</p>
    <p class="person__role">Team Leader</p>
  </div>
  <div class="contact-panel">
    <div class="contact-panel__col">
      <svg viewBox="0 0 24 24" fill="none" stroke="#fff" stroke-width="1.6" stroke-linejoin="round">
        <path d="M3 9c0-2 4-4 9-4s9 2 9 4v1.5h-4V9c-1.5-.7-3-1-5-1s-3.5.3-5 1v1.5H3z"/>
        <path d="M6 12h12l2 7H4z"/><circle cx="12" cy="15.5" r="1.8"/>
      </svg>
      <p>012 555 0148<br>012 555 0148</p>
    </div>
    <div class="contact-panel__col">
      <svg viewBox="0 0 24 24" fill="none" stroke="#fff" stroke-width="1.6">
        <circle cx="12" cy="12" r="9"/><ellipse cx="12" cy="12" rx="4" ry="9"/>
        <path d="M3 12h18M5 7h14M5 17h14"/>
      </svg>
      <p>info@brightharbordentalcare.example<br>brightharbordentalcare.example</p>
    </div>
    <div class="contact-panel__col">
      <svg viewBox="0 0 24 24" fill="#fff">
        <path d="M12 2a7 7 0 0 0-7 7c0 5 7 13 7 13s7-8 7-13a7 7 0 0 0-7-7zm0 9.5A2.5 2.5 0 1 1 12 6.5a2.5 2.5 0 0 1 0 5z"/>
      </svg>
      <p>2847 NW 42nd Ave<br>Del City, OK 73115</p>
    </div>
  </div>
</section>

</body>
</html>
```